依頼詳細
制作条件は下記の通り。
1)スマホのトップページのデザイン。ただしトップページ全体の制作は不要で、原則は最初に表示される画面のみでよい。ただしデザインをよりわかりやすくするために、最初に表示される画面に加えてその下部の若干のデザインを含むのは自由。
2)ロゴは添付のデータを用いる。
3)指定色のレッドをブランドカラーとして強調し、サイト名の中にある「+」を象徴的に使うことが望ましい。
4)既存マッチングサイトとは一線を画する、斬新なイメージであること。
5)都会的で洗練されたデザインであるとともに、見た目の美しさだけのレベルにとどまらず、「おー!」と見た人を驚かせるようなインパクトのあるデザインであること。
6)モデル撮影やレンタルフォトの使用なども可能。その場合はダミーのイメージを置いておく。
7)キャッチコピーがあったほうがよい場合はダミーのコピーを置いておく。
8)デザインは添付の「スマホ画面」の画面にレイアウトして、JPEGデータで提出。
ページ数
1ページ
希望イメージ
シンプル 複雑
単色 カラフル
暗い 明るい
日常 高級
遊び心 厳粛
未来的 伝統的
女性的 男性的
希望する色
赤系
補足説明
最終納品はイラストレーター形式ですが、応募はJPEGにてお願いします。
添付の「スマホ画面」の画面にレイアウトしてください。
たくさんの応募をいただきましたが、従来のマッチングサイトとは異なる「斬新」「サプライズ」という点で該当するものがあまりありませんでした。
つきましては、期間延長をさせていだきますので、この点をご理解をいただき私たちを「あっ!」っと言わせるような作品を応募いただけることを願っております。
■ 選んだ理由

シンプルで操作性に秀でた作品だと感じました。

■ 提案者全員のお礼・コメント

みなさま、
たくさんの素敵な作品をありがとうございました!

```html
<!DOCTYPE html>
<html lang="ja">
<head>
<meta charset="utf-8">
<title>KIZUNA+ トップ</title>
<link rel="stylesheet" href="https://fonts.googleapis.com/css2?family=Noto+Sans+JP:wght@500;700&display=swap">
<style>
  :root {
    --brand-red: #c8102e;
    --deep-red: #a80c24;
    --shadow-red: #7a0a1b;
    --white: #ffffff;
    --photo-warm-1: #8e8478;
    --photo-warm-2: #d9d2c6;
    --photo-cool-1: #5e5f60;
    --photo-cool-2: #a6a29b;
  }
  html, body {
    margin: 0;
    padding: 0;
    width: 1200px;
    height: 2216px;
    overflow: hidden;
    background: var(--brand-red);
  }
  .hero {
    position: relative;
    width: 1200px;
    height: 2216px;
    overflow: hidden;
    background: var(--brand-red);
    font-family: "Noto Sans JP", sans-serif;
    color: var(--white);
  }
  .hero__bands {
    position: absolute;
    inset: 0;
  }
  .brand {
    position: absolute;
    left: 110px;
    top: 150px;
    display: flex;
    align-items: center;
    gap: 22px;
  }
  .brand__square {
    width: 34px;
    height: 34px;
    background: var(--white);
  }
  .brand__name {
    font-size: 58px;
    font-weight: 700;
    letter-spacing: 0.06em;
    line-height: 1;
  }
  .photo {
    position: absolute;
  }
  .photo--edge-right {
    left: 1128px; top: 0; width: 72px; height: 1230px;
    background: linear-gradient(180deg, var(--shadow-red), #5c0814 60%, var(--deep-red));
    opacity: 0.85;
  }
  .photo--edge-left {
    left: 0; top: 1070px; width: 150px; height: 860px;
    background: linear-gradient(180deg, #5c0814, var(--shadow-red) 50%, #4a0610);
    opacity: 0.9;
  }
  .photo--man {
    left: 600px; top: 370px; width: 515px; height: 990px;
    background: linear-gradient(160deg, var(--photo-cool-2), var(--photo-cool-1) 70%, #3c3b3a);
  }
  .photo--woman {
    left: 145px; top: 720px; width: 455px; height: 990px;
    background: linear-gradient(170deg, #4d5560, var(--photo-warm-1) 45%, var(--photo-warm-2));
    box-shadow: 0 10px 30px rgba(0,0,0,0.25);
  }
  .tagline {
    position: absolute;
    left: 335px;
    top: 1820px;
  }
  .tagline__ja {
    margin: 0;
    font-size: 72px;
    font-weight: 700;
    letter-spacing: 0.08em;
    line-height: 1.2;
  }
  .tagline__en {
    margin: 10px 0 0;
    font-size: 46px;
    font-weight: 500;
    letter-spacing: 0.02em;
  }
  .scroll-cue {
    position: absolute;
    right: 0;
    bottom: 0;
    width: 270px;
    height: 260px;
  }
</style>
</head>
<body>
<main class="hero">
  <svg class="hero__bands" width="1200" height="2216" viewBox="0 0 1200 2216" aria-hidden="true">
    <polygon points="0,0 1200,0 1200,420 0,1500" fill="var(--deep-red)" opacity="0.45"/>
    <polygon points="700,0 1200,0 1200,1100" fill="var(--shadow-red)" opacity="0.35"/>
    <polygon points="0,1500 1200,420 1200,700 0,1800" fill="#d21733" opacity="0.35"/>
  </svg>

  <div class="brand">
    <span class="brand__square"></span>
    <span class="brand__name">KIZUNA+</span>
  </div>

  <div class="photo photo--edge-right" role="img" aria-label="赤く色づけた男性の横顔の写真の一部"></div>
  <div class="photo photo--edge-left" role="img" aria-label="赤く色づけた人物写真の一部"></div>
  <div class="photo photo--man" role="img" aria-label="白いカップを手に持つ髭の男性の写真"></div>
  <div class="photo photo--woman" role="img" aria-label="白いレースの服で微笑む女性の写真"></div>

  <div class="tagline">
    <p class="tagline__ja">ここから、つながる。</p>
    <p class="tagline__en">Together. Forever.</p>
  </div>

  <svg class="scroll-cue" viewBox="0 0 270 260" aria-label="下へスクロール">
    <polygon points="270,0 270,260 0,260" fill="var(--white)"/>
    <polyline points="172,168 198,194 224,168" fill="none" stroke="var(--brand-red)" stroke-width="7" stroke-linecap="round" stroke-linejoin="round"/>
  </svg>
</main>
</body>
</html>
```